依頼詳細
当社のリーフレットやウェブサイトやその他資料に基づいたデザインでお願い致します。
記載項目
榊原会館 月照苑 有限会社みのり堂
https://gessho-en.example/
サイズ
A4
ページ数
4ページ
希望イメージ
シンプル 複雑
単色 カラフル
暗い 明るい
日常 高級
遊び心 厳粛
未来的 伝統的
女性的 男性的
希望する色
青系、水色系、無彩色系
納品ファイル
補足説明
■ 選んだ理由

この度の提案では従業員一同ぼんやりとイメージがありそれに一番近かった、またごちゃごちゃしていないデザイン、お花のチョイスなども決め手でした。

■ 提案者全員のお礼・コメント

はじめての依頼になりましたが、少量のページ数ながらみなさんのご提案はすばらしかったです。
資料を具体的にわかりやすくご提案いただいたのに採用できないことは非常に残念に感じます。
この度は誠にありがとうございました。

```html
<!DOCTYPE html>
<html lang="ja">
<head>
<meta charset="UTF-8">
<title>月照苑 セレモニーサービスのご案内</title>
<link rel="stylesheet" href="https://fonts.googleapis.com/css2?family=Noto+Sans+JP:wght@400;500;700&family=Shippori+Mincho:wght@500;700;800&display=swap">
<style>
  :root {
    --paper: #ffffff;
    --mist: #f1f2f4;
    --navy: #1d3570;
    --sky: #2e8fd3;
    --ink: #333333;
    --grey: #8a8a8a;
    --gold-light: #e9cf7a;
    --gold-dark: #b8912f;
    --badge-blue: #3c9ad8;
    --pattern: #e4e8ee;
  }
  * { margin: 0; padding: 0; box-sizing: border-box; }
  html, body { width: 846px; height: 1200px; overflow: hidden; }
  body { background: var(--paper); font-family: "Noto Sans JP", sans-serif; color: var(--ink); }

  .cover {
    position: relative; width: 846px; height: 1200px; overflow: hidden;
    background: radial-gradient(ellipse at 50% 40%, var(--paper) 35%, var(--mist) 100%);
  }
  .wave-pattern {
    position: absolute; top: 0; right: 0; width: 200px; height: 520px;
    background: linear-gradient(200deg, var(--pattern) 0%, rgba(228,232,238,0) 70%);
  }
  .edition {
    position: absolute; left: 40px; top: 34px; width: 72px; height: 28px;
    border: 1px solid var(--grey); color: var(--grey);
    font-size: 14px; line-height: 26px; text-align: center; letter-spacing: 0.1em;
  }
  .company {
    position: absolute; right: 48px; top: 66px;
    font-family: "Shippori Mincho", serif; color: var(--ink);
    display: flex; align-items: baseline; gap: 8px;
  }
  .company .type { font-size: 16px; }
  .company .name { font-size: 30px; font-weight: 700; }

  .title-block { position: absolute; left: 0; right: 0; top: 268px; text-align: center; }
  .venue {
    position: absolute; left: 262px; top: 0;
    font-size: 15px; color: var(--ink); letter-spacing: 0.05em;
  }
  .facility {
    margin-top: 26px;
    font-family: "Shippori Mincho", serif; font-weight: 800;
    font-size: 118px; color: var(--navy); letter-spacing: 0.06em; line-height: 1.1;
  }
  .tagline {
    margin-top: 70px; font-size: 26px; font-weight: 500;
    color: var(--sky); letter-spacing: 0.08em;
  }

  .staff-photo {
    position: absolute; left: 150px; top: 690px; width: 330px; height: 510px;
    background: linear-gradient(180deg, #e9ecef 0%, #f4f4f4 40%, #d9dde3 100%);
    border-radius: 160px 160px 0 0;
  }

  .badges { position: absolute; top: 934px; left: 506px; display: flex; gap: 14px; align-items: center; }
  .badge {
    border-radius: 50%; display: flex; flex-direction: column;
    align-items: center; justify-content: center; color: #fff; text-align: center;
  }
  .badge--score {
    width: 98px; height: 98px;
    background: radial-gradient(circle at 35% 30%, var(--gold-light), var(--gold-dark));
  }
  .badge--score .label { font-size: 10px; line-height: 1.2; }
  .badge--score .value { font-size: 36px; font-weight: 700; line-height: 1; }
  .badge--score .value small { font-size: 14px; }
  .badge--service {
    width: 80px; height: 80px; background: var(--badge-blue);
    font-size: 17px; font-weight: 700; line-height: 1.25;
  }
  .footnote {
    position: absolute; left: 506px; top: 1150px;
    font-size: 10px; color: var(--grey);
  }
</style>
</head>
<body>
<main class="cover">
  <div class="wave-pattern" role="img" aria-label="右上に淡い波文様の装飾"></div>

  <div class="edition">初版</div>

  <header class="company">
    <span class="type">有限会社</span><span class="name">みのり堂</span>
  </header>

  <section class="title-block">
    <p class="venue">榊原会館</p>
    <h1 class="facility">月照苑</h1>
    <p class="tagline">セレモニーサービスのご案内</p>
  </section>

  <div class="staff-photo" role="img" aria-label="白いシャツ姿の男女二人のスタッフ写真"></div>

  <div class="badges">
    <div class="badge badge--score">
      <span class="label">お客様満足度※1</span>
      <span class="value">99<small>%</small></span>
    </div>
    <div class="badge badge--service">年中<br>無休</div>
    <div class="badge badge--service">24時間<br>対応</div>
  </div>

  <p class="footnote">※1 調査期間 20XX年XX月〜XX月 合計</p>
</main>
</body>
</html>
```